QWTORAMX ( Wordpress website for catalogue of Zintrop Cast Pages)

Need a website to showcase different Zintrop Cast pages ( in different categories). Similar to e-commerce except no check-out / purchase of items. Pls use our logos provided and color scheme to be white+red+ blue as per our logo.

Target Market(s)

Consumers

Font styles to use
Sans Serif

Colors
ffffff
ec1f27
3276b5

Requirements
Must have
• I will need a Wordpress Theme as a handover. Also, pls use the color scheme (red+blue+white) as per logo attached. Prefer clean and near design with white space.

```html
<!DOCTYPE html>
<html lang="en">
<head>
<meta charset="utf-8">
<title>QWTORAMX</title>
<link href="https://fonts.googleapis.com/css2?family=Lato:wght@400;700;900&family=Roboto+Condensed:wght@700&display=swap" rel="stylesheet">
<style>
:root{
  --red:#ec1f27;
  --red-soft:#e8264f;
  --blue:#3276b5;
  --blue-bright:#1f6fe0;
  --band-blue:#3a7fe0;
  --ink:#1a1a1a;
  --muted:#777;
  --footer:#474747;
  --white:#ffffff;
  --hero-pink:#ea7fa0;
}
*{box-sizing:border-box;margin:0;padding:0}
html,body{width:1200px;height:2745px;overflow:hidden}
body{position:relative;background:var(--white);font-family:'Lato',sans-serif;color:var(--ink)}
.abs{position:absolute}
.head-font{font-family:'Roboto Condensed',sans-serif;font-weight:700}

/* header */
.site-header{left:0;top:0;width:1200px;height:72px;background:var(--white)}
.brand{left:110px;top:18px;font-size:30px;font-weight:900;color:var(--blue-bright);letter-spacing:-0.5px}
.main-nav{left:387px;top:26px;display:flex;gap:29px;font-size:14.5px;font-weight:700}
.main-nav a{color:var(--ink);text-decoration:none}
.main-nav a.current{color:var(--blue-bright)}
.login{left:963px;top:12px;width:118px;height:47px;border-radius:24px;background:var(--red);color:var(--white);font-size:14.5px;font-weight:700;display:flex;align-items:center;justify-content:center;gap:10px}

/* hero */
.hero{left:0;top:72px;width:1200px;height:559px;background:radial-gradient(ellipse at 50% 45%,#f07ea3 0%,#e86c93 55%,#d7658e 100%);text-align:center;color:var(--white)}
.hero h1{position:absolute;left:0;right:0;top:152px;font-size:78px;letter-spacing:1px}
.hero p{position:absolute;left:220px;width:760px;top:257px;font-size:19px;line-height:28px}
.btn-start{left:515px;top:340px;width:170px;height:50px;border-radius:25px;background:var(--red);font-size:14.5px;font-weight:700;display:flex;align-items:center;justify-content:center;gap:12px}
.dots{left:570px;top:486px;display:flex;gap:4px}
.dots span{width:10px;height:10px;border-radius:50%;background:var(--white)}
.dots span.on{background:transparent;border:2px solid var(--white)}

/* service tiles */
.tile{top:722px;width:187px;height:176px;background:var(--white);box-shadow:0 0 6px rgba(0,0,0,.18);text-align:center}
.tile svg{margin-top:28px}
.tile .label{position:absolute;left:0;right:0;top:130px;font-size:20px;color:var(--ink)}
.tile.active{background:linear-gradient(180deg,#2d6fe0 0%,#9b3b94 55%,#ec1f4f 100%)}
.tile.active .label{color:var(--white)}

/* category band */
.band{left:0;top:987px;width:1200px;height:531px;background:var(--band-blue)}
.band h2{position:absolute;left:0;right:0;top:76px;text-align:center;color:var(--white);font-size:54px}
.card{top:180px;width:235px;height:259px;border:3px solid #e8eef8}
.card .live{position:absolute;right:22px;top:14px;font-size:15px;color:var(--white)}
.card .name{position:absolute;left:0;right:0;bottom:32px;text-align:center;color:var(--white);font-size:20px}
.arrow{top:289px;width:43px;height:43px;border-radius:50%;background:var(--white);display:flex;align-items:center;justify-content:center}

/* quote */
.quote-photo{left:505px;top:1622px;width:558px;height:581px;background:linear-gradient(135deg,#4a3326 0%,#8e4a2c 40%,#e06a3c 60%,#6b4a35 100%)}
.quote-card{left:137px;top:1678px;width:483px;height:409px;background:var(--white);box-shadow:0 0 6px rgba(0,0,0,.12)}
.quote-card h3{position:absolute;left:52px;top:32px;font-size:40px;letter-spacing:.5px}
.field{position:absolute;border:1px solid #e2e2e2;font-size:13px;color:#666;padding:13px 14px}
.btn-dl{left:54px;top:318px;width:166px;height:44px;border-radius:22px;background:var(--red);color:var(--white);font-size:15px;font-weight:700;display:flex;align-items:center;justify-content:center}
.call-box{left:285px;top:2087px;width:335px;height:116px;background:var(--blue-bright);color:var(--white)}
.call-box .t1{position:absolute;left:109px;top:24px;font-size:20px}
.call-box .t2{position:absolute;left:109px;top:54px;font-size:37px;font-weight:700}

/* footer */
.site-footer{left:0;top:2296px;width:1200px;height:449px;background:var(--footer);color:var(--white)}
.f-title{position:absolute;top:70px;font-size:14.5px;font-weight:700}
.f-row{position:absolute;left:180px;display:flex;align-items:flex-start;gap:20px;font-size:15px;line-height:22px}
.f-ico{width:34px;height:34px;border-radius:50%;background:var(--white);display:flex;align-items:center;justify-content:center;flex:none}
.f-brand{left:508px;top:130px;font-size:48px;font-weight:900;color:var(--blue-bright);letter-spacing:-1px}
.socials{left:546px;top:227px;display:flex;gap:3px}
.socials span{width:42px;height:42px;border-radius:50%;background:var(--white)}
.quick{position:absolute;right:180px;text-align:right;font-size:15px}
.quick li{list-style:none;height:34.5px}
.quick li::after{content:"\00AB";margin-left:14px}
.rule{left:109px;top:331px;width:978px;height:1px;background:#bdbdbd}
.copy{left:0;right:0;top:370px;text-align:center;font-size:15px}
</style>
</head>
<body>

<header class="abs site-header">
  <div class="abs brand">QWTORAMX</div>
  <nav class="abs main-nav">
    <a class="current" href="#">HOME</a><a href="#">ABOUT US</a><a href="#">LATEST BLOG</a><a href="#">REVIEWS</a><a href="#">CONTACT US</a>
  </nav>
  <div class="abs login">LOG IN
    <svg width="11" height="13" viewBox="0 0 11 13"><rect x="0" y="5" width="11" height="8" rx="1" fill="#fff"/><path d="M2.5 5V3.5a3 3 0 0 1 6 0V5" stroke="#fff" stroke-width="1.6" fill="none"/></svg>
  </div>
</header>

<section class="abs hero" role="img" aria-label="Flat-lay of fashion accessories, shoes, bag, watch and flowers on pink background">
  <h1 class="head-font">QWTORAMX</h1>
  <p>Lorem ipsum dolor sit amet, consectetur adipiscing elit, sed do eiusmod tempor incididunt ut labore et dolore magna aliqua. Ut enim ad minim veniam, quis nostrud</p>
  <div class="abs btn-start">GET STARTED
    <svg width="14" height="14" viewBox="0 0 14 14"><circle cx="7" cy="7" r="7" fill="#fff"/><path d="M5.5 4l3 3-3 3" stroke="#ec1f27" stroke-width="1.8" fill="none"/></svg>
  </div>
  <div class="abs dots"><span></span><span></span><span class="on"></span><span></span><span></span></div>
</section>

<svg width="0" height="0" style="position:absolute">
  <defs>
    <linearGradient id="ig" x1="0" y1="0" x2="1" y2="1"><stop offset="0" stop-color="#2d6fe0"/><stop offset="1" stop-color="#ec1f4f"/></linearGradient>
  </defs>
</svg>

<div class="abs tile" style="left:109px">
  <svg width="72" height="68" viewBox="0 0 72 68" fill="none" stroke="url(#ig)" stroke-width="2.2"><path d="M4 18l26-12 26 12v30L30 60 4 48z"/><path d="M4 18l26 12 26-12M30 30v30"/><rect x="44" y="30" width="24" height="34" rx="2" fill="#fff"/><path d="M49 38h4M56 38h8M49 46h4M56 46h8M49 54h4M56 54h8"/></svg>
  <div class="label head-font">ORDERS</div>
</div>
<div class="abs tile" style="left:308px">
  <svg width="68" height="68" viewBox="0 0 68 68" fill="none" stroke="url(#ig)" stroke-width="2.2"><rect x="8" y="4" width="52" height="10"/><path d="M6 14h56l-3 10H9z"/><path d="M10 24v38h50V24"/><rect x="36" y="32" width="18" height="14"/><rect x="16" y="34" width="14" height="28"/><circle cx="14" cy="54" r="9" fill="#fff"/><path d="M10 58l8-8"/></svg>
  <div class="label head-font">PROMOS</div>
</div>
<div class="abs tile active" style="left:507px">
  <svg width="64" height="72" viewBox="0 0 64 72" fill="none" stroke="#fff" stroke-width="2.2"><circle cx="32" cy="26" r="22"/><circle cx="32" cy="26" r="14"/><path d="M32 17l3 6 6 1-4.5 4 1 6-5.5-3-5.5 3 1-6-4.5-4 6-1z"/><path d="M16 42L6 64l10-3 5 9 8-20M48 42l10 22-10-3-5 9-8-20"/></svg>
  <div class="label head-font">REWARDS</div>
</div>
<div class="abs tile" style="left:706px">
  <svg width="68" height="68" viewBox="0 0 68 68" fill="none" stroke="url(#ig)" stroke-width="2.4"><path d="M14 6l10 14-6 6c3 8 10 15 18 18l6-6 14 10-6 10C26 58 6 38 4 14z"/><path d="M36 16a16 16 0 0 1 16 16M36 6a26 26 0 0 1 26 26"/></svg>
  <div class="label head-font">CALL US</div>
</div>
<div class="abs tile" style="left:904px">
  <svg width="72" height="72" viewBox="0 0 72 72" fill="none" stroke="url(#ig)" stroke-width="2.2"><path d="M36 4v66M30 70h12"/><path d="M6 12h56l5 5-5 5H6z"/><path d="M66 30H12l-5 5 5 5h54z"/><path d="M10 48h46l4 4-4 4H10z"/></svg>
  <div class="label head-font">DIRECTIONS</div>
</div>

<section class="abs band" role="img" aria-label="Blue-tinted backdrop of vegetables and herbs">
  <h2 class="head-font">QWTORAMX</h2>
  <div class="abs card" style="left:108px;background:linear-gradient(160deg,#8fa3b5,#c9d4dc 60%,#b9bfc4)" role="img" aria-label="Fluffy headband accessory">
    <span class="live">LIVE</span><span class="name head-font">GIRL ACCESSORIES</span></div>
  <div class="abs card" style="left:358px;background:linear-gradient(160deg,#55605a,#8b8c84 55%,#6a5a4c)" role="img" aria-label="Dresses on display">
    <span class="live">LIVE</span><span class="name head-font">VELLORA BOUTIQUE</span></div>
  <div class="abs card" style="left:607px;background:linear-gradient(160deg,#6d6a66,#9a958d 55%,#5c5852)" role="img" aria-label="Shelves of boxed electronics">
    <span class="live">LIVE</span><span class="name head-font">ELECTRONICS</span></div>
  <div class="abs card" style="left:857px;background:linear-gradient(160deg,#5a6a84,#8c96a4 55%,#4c5670)" role="img" aria-label="Store shelves of boxed gadgets">
    <span class="live">LIVE</span><span class="name head-font">GADGETS</span></div>
  <div class="abs arrow" style="left:31px"><svg width="14" height="20" viewBox="0 0 14 20"><path d="M11 2L3 10l8 8" stroke="#111" stroke-width="2.4" fill="none"/></svg></div>
  <div class="abs arrow" style="left:1126px"><svg width="14" height="20" viewBox="0 0 14 20"><path d="M3 2l8 8-8 8" stroke="#111" stroke-width="2.4" fill="none"/></svg></div>
</section>

<div class="abs quote-photo" role="img" aria-label="Fresh salmon, tomatoes, garlic, almonds and olive oil on wooden board"></div>

<section class="abs quote-card">
  <h3 class="head-font">GET A FREE QUOTE</h3>
  <div class="field" style="left:54px;top:107px;width:180px;height:42px">Name</div>
  <div class="field" style="left:245px;top:107px;width:180px;height:42px">Phone No</div>
  <div class="field" style="left:54px;top:158px;width:367px;height:43px">Email Address</div>
  <div class="field" style="left:54px;top:213px;width:367px;height:86px">Message</div>
  <div class="abs btn-dl">DOWNLOAD NOW</div>
</section>
<div class="abs call-box">
  <svg class="abs" style="left:24px;top:30px" width="58" height="58" viewBox="0 0 68 68" fill="none" stroke="#fff" stroke-width="2.4"><path d="M14 6l10 14-6 6c3 8 10 15 18 18l6-6 14 10-6 10C26 58 6 38 4 14z"/><path d="M36 16a16 16 0 0 1 16 16M36 6a26 26 0 0 1 26 26"/></svg>
  <div class="t1">Get a Free Quote Today</div>
  <div class="t2">555.014.2738</div>
</div>

<footer class="abs site-footer">
  <div class="f-title" style="left:180px">CONTACT US</div>
  <div class="f-row" style="top:115px">
    <span class="f-ico"><svg width="14" height="18" viewBox="0 0 14 18"><path d="M7 0a7 7 0 0 1 7 7c0 5-7 11-7 11S0 12 0 7a7 7 0 0 1 7-7z" fill="#1f6fe0"/><circle cx="7" cy="7" r="2.5" fill="#fff"/></svg></span>
    <span>120 , Lorem Ipsum Dolor<br>United States</span>
  </div>
  <div class="f-row" style="top:200px">
    <span class="f-ico"><svg width="16" height="16" viewBox="0 0 16 16"><path d="M3 1l3 4-2 2c1 2 3 4 5 5l2-2 4 3-2 3C6 15 1 10 1 3z" fill="#1f6fe0"/></svg></span>
    <span style="margin-top:6px">1 555 010 447</span>
  </div>
  <div class="f-row" style="top:245px">
    <span class="f-ico"><svg width="16" height="12" viewBox="0 0 16 12" fill="none" stroke="#1f6fe0" stroke-width="1.6"><rect x="1" y="1" width="14" height="10" rx="1"/><path d="M1 2l7 5 7-5"/></svg></span>
    <span style="margin-top:6px">info@qwtoramx.com</span>
  </div>

  <div class="abs f-brand">QWTORAMX</div>
  <div class="abs socials" aria-label="Social links"><span></span><span></span><span></span><span></span></div>

  <div class="f-title" style="right:180px">QUICK LINKS</div>
  <ul class="quick" style="top:110px">
    <li>Home</li><li>About Us</li><li>Contact Us</li><li>Girls Accessories</li><li>Help Service</li>
  </ul>

  <div class="abs rule"></div>
  <div class="abs copy">© 2020 Qwtoramx. All Rights Reserved</div>
</footer>

</body>
</html>
```